Health & Wellness Contest - The Bright Harvest Renewal

We need a postcard design that is professional and grabs the attention of people who see it. The postcard will be left in fitness centers and posted on social media. The front of the card MUST look amazing - make potential participants want to pick it up and find out more information; the back of the card will have the contest details. The goal is to have people sign up for a 90 day fitness program, and most of the marketing will be with this postcard.

Target Market(s)

People that are thinking about beginning a health regiment; people who are already used to exercising and are willing to try a new supplement

Industry/Entity Type

Health And Wellness

Colors

Designer to choose colors to be used in the design.

Requirements
Must have
• Front Cover -- Must have the phrase "The Bright Harvest Renewal" and must have "$2,500 Grand Prize"; and must have "BrightHarvestRenewal.com"
Nice to have
• Design on Front; Details on Back; appeal to both men and women

```html
<!DOCTYPE html>
<html lang="en">
<head>
<meta charset="utf-8">
<title>The Bright Harvest Renewal – Postcard</title>
<link rel="stylesheet" href="https://fonts.googleapis.com/css2?family=Montserrat:wght@500;700&family=Open+Sans:wght@400;600;700;800&family=Roboto+Condensed:wght@700&display=swap">
<style>
  :root {
    --page: #ececec;
    --card-white: #ffffff;
    --panel-dark: #2b2b2b;
    --edge-grey: #a3a7ab;
    --brand-blue: #2f6fb8;
    --brand-blue-deep: #1d4f8f;
    --brand-blue-light: #4b8fd6;
    --text-white: #ffffff;
    --text-soft: #d9d9d9;
    --silver-top: #ffffff;
    --silver-bottom: #9a9a9a;
  }
  * { box-sizing: border-box; margin: 0; padding: 0; }
  html, body { width: 802px; height: 1200px; overflow: hidden; }
  body { background: var(--page); font-family: "Open Sans", sans-serif; position: relative; }

  .postcard {
    position: absolute; left: 73px; width: 656px; height: 505px;
    background: var(--card-white); padding: 14px;
    box-shadow: 0 4px 14px rgba(0,0,0,.25);
  }
  .postcard--front { top: 123px; }
  .postcard--back  { top: 654px; }
  .postcard__inner { position: relative; width: 628px; height: 477px; overflow: hidden; }
  .postcard__shapes { position: absolute; inset: 0; }

  .brand { position: absolute; display: flex; flex-direction: column; align-items: center; color: var(--text-white); }
  .brand__mark { width: 30px; height: 30px; background: var(--brand-blue); margin-bottom: 8px; }
  .brand__name { font-family: "Montserrat", sans-serif; font-weight: 500; font-size: 20px; letter-spacing: 1px; line-height: 1; }
  .brand__tag { font-family: "Montserrat", sans-serif; font-weight: 500; font-size: 10px; letter-spacing: 2.5px; margin-top: 3px; color: var(--text-soft); }

  /* Front */
  .front-brand { left: 22px; top: 28px; width: 220px; }
  .headline { position: absolute; left: 0; width: 325px; text-align: center; font-weight: 800; line-height: 1; }
  .headline span {
    background: linear-gradient(180deg, var(--silver-top), var(--silver-bottom));
    -webkit-background-clip: text; background-clip: text; color: transparent;
  }
  .headline--main { top: 152px; font-size: 42px; letter-spacing: 1px; }
  .headline--sub  { top: 206px; font-size: 26px; letter-spacing: .5px; }
  .prize { position: absolute; left: 0; top: 266px; width: 270px; text-align: center; font-family: "Roboto Condensed", sans-serif; font-weight: 700; color: var(--text-white); text-shadow: 0 2px 3px rgba(0,0,0,.35); line-height: 1; }
  .prize__amount { font-size: 72px; }
  .prize__label { font-size: 38px; margin-top: 6px; }
  .url-bar {
    position: absolute; left: 0; top: 412px; width: 245px; height: 25px;
    background: var(--brand-blue); color: var(--text-white);
    font-weight: 700; font-size: 14.5px; line-height: 25px; padding-left: 13px;
  }

  /* Back */
  .back-brand { left: 68px; top: 8px; width: 150px; }
  .back-brand .brand__mark { width: 22px; height: 22px; margin-bottom: 5px; }
  .back-brand .brand__name { font-size: 14px; }
  .back-brand .brand__tag { font-size: 7px; letter-spacing: 1.8px; }
  .details { position: absolute; left: 16px; top: 78px; width: 370px; color: var(--text-white); font-size: 14px; line-height: 20px; }
  .details p + p { margin-top: 8px; }
  .benefits { list-style: none; margin-top: 8px; }
  .benefits li { position: relative; padding-left: 30px; line-height: 20.4px; }
  .benefits li::before { content: "✓"; position: absolute; left: 2px; top: 0; }
  .contact { position: absolute; left: 16px; top: 387px; color: var(--text-white); font-size: 14px; line-height: 20px; }
  .contact__deadline strong { display: block; font-weight: 700; }
  .contact__line { display: flex; align-items: center; gap: 5px; font-weight: 700; margin-top: 4px; }
  .contact__icon { width: 17px; height: 17px; flex: none; }
</style>
</head>
<body>

<section class="postcard postcard--front">
  <div class="postcard__inner">
    <svg class="postcard__shapes" width="628" height="477" viewBox="0 0 628 477">
      <defs>
        <linearGradient id="parkGreen" x1="0" y1="0" x2="0" y2="1">
          <stop offset="0" stop-color="#7f9f5e"/>
          <stop offset=".5" stop-color="#4d7a33"/>
          <stop offset="1" stop-color="#6a8a45"/>
        </linearGradient>
        <linearGradient id="prizeBlue" x1="0" y1="0" x2="0" y2="1">
          <stop offset="0" stop-color="#4b8fd6"/>
          <stop offset="1" stop-color="#1d4f8f"/>
        </linearGradient>
      </defs>
      <rect width="628" height="477" fill="url(#parkGreen)" role="img" aria-label="Photo: a man and a woman jogging together on a green park path"/>
      <polygon points="0,0 237,0 403,146 237,477 0,477" fill="#a3a7ab"/>
      <polygon points="0,0 225,0 391,146 225,477 0,477" fill="#2b2b2b"/>
      <polygon points="0,255 336,255 260,408 0,408" fill="url(#prizeBlue)"/>
    </svg>

    <div class="brand front-brand">
      <div class="brand__mark"></div>
      <div class="brand__name">NORTHVALE</div>
      <div class="brand__tag">AREAS OF PRACTICE</div>
    </div>

    <h1 class="headline headline--main"><span>THE BRIGHT</span></h1>
    <h2 class="headline headline--sub"><span>HARVEST RENEWAL</span></h2>

    <div class="prize">
      <div class="prize__amount">$2,500</div>
      <div class="prize__label">GRAND PRIZE</div>
    </div>

    <div class="url-bar">www.BrightHarvestRenewal.com</div>
  </div>
</section>

<section class="postcard postcard--back">
  <div class="postcard__inner">
    <svg class="postcard__shapes" width="628" height="477" viewBox="0 0 628 477">
      <defs>
        <linearGradient id="autumnPark" x1="0" y1="0" x2="0" y2="1">
          <stop offset="0" stop-color="#e3a43a"/>
          <stop offset=".5" stop-color="#c9873a"/>
          <stop offset="1" stop-color="#7f9a48"/>
        </linearGradient>
      </defs>
      <rect width="628" height="477" fill="url(#autumnPark)" role="img" aria-label="Photo: a woman in red running gear and a man jogging through an autumn park"/>
      <polygon points="0,0 284,0 435,143 293,477 0,477" fill="#a3a7ab"/>
      <polygon points="0,0 272,0 423,143 281,477 0,477" fill="#2b2b2b"/>
      <polygon points="0,382 321,382 281,477 0,477" fill="#2f6fb8"/>
    </svg>

    <div class="brand back-brand">
      <div class="brand__mark"></div>
      <div class="brand__name">NORTHVALE</div>
      <div class="brand__tag">AREAS OF PRACTICE</div>
    </div>

    <div class="details">
      <p>The Bright Harvest Renewal has one mission – to help people be a better version of themselves.</p>
      <p>Join us in the Bright Harvest Renewal and experience some of the benefits that countless others have seen:</p>
      <ul class="benefits">
        <li>Better health</li>
        <li>Appetite suppression</li>
        <li>Better energy</li>
        <li>Fat Loss</li>
        <li>Better focus</li>
        <li>Increased awareness</li>
        <li>Better mood</li>
        <li>Muscle preservation</li>
        <li>Better sleep</li>
      </ul>
    </div>

    <div class="contact">
      <div class="contact__deadline">Challenge Deadline: Register by <strong>October 31, 2017</strong></div>
      <div class="contact__line">
        <svg class="contact__icon" viewBox="0 0 17 17"><circle cx="8.5" cy="8.5" r="8.5" fill="#fff"/><rect x="4" y="5.5" width="9" height="6" fill="none" stroke="#2f6fb8" stroke-width="1.2"/><polyline points="4,5.5 8.5,9 13,5.5" fill="none" stroke="#2f6fb8" stroke-width="1.2"/></svg>
        <span>Info@NorthvaleGroup.org</span>
      </div>
      <div class="contact__line">
        <svg class="contact__icon" viewBox="0 0 17 17"><circle cx="8.5" cy="8.5" r="8.5" fill="#fff"/><circle cx="8.5" cy="8.5" r="4.8" fill="none" stroke="#2f6fb8" stroke-width="1.1"/><ellipse cx="8.5" cy="8.5" rx="2" ry="4.8" fill="none" stroke="#2f6fb8" stroke-width="1"/><line x1="3.7" y1="8.5" x2="13.3" y2="8.5" stroke="#2f6fb8" stroke-width="1"/></svg>
        <span>www.BrightHarvestRenewal.com</span>
      </div>
    </div>
  </div>
</section>

</body>
</html>
```